Document Proposal to be designed with Graphics and Professional looking

This is a letter to be sent to generate interest as a proposal for a Pharmaceutical Sale. The figure in the document are from different articles explaining the systems I will attach pictures. I am not sure if I want to use my official Logo, please feel free to place something appropriate for illustration purposes only

```html
<!DOCTYPE html>
<html lang="en">
<head>
<meta charset="utf-8">
<title>Pharmaceutical Distribution Proposal</title>
<link href="https://fonts.googleapis.com/css2?family=Lato:wght@400;700;900&family=Oswald:wght@500;600&display=swap" rel="stylesheet">
<style>
:root{
  --canvas:#ebebeb;
  --paper:#ffffff;
  --blue:#3f6fd1;
  --blue-deep:#2f5bc4;
  --cyan:#15a9e6;
  --cyan-light:#2fb8f0;
  --red:#e3101b;
  --ink:#2b2b2b;
  --link:#1c6fc9;
  --navy:#1f3566;
  --row:#1f4c8f;
  --green:#7cc242;
  --muted:#e4e8ee;
}
*{box-sizing:border-box;margin:0;padding:0}
html,body{width:1200px;height:2262px;overflow:hidden;background:var(--canvas)}
body{position:relative;font-family:"Lato",Arial,sans-serif;color:var(--ink)}
.page{position:absolute;width:486px;height:632px;background:var(--paper);box-shadow:0 1px 5px rgba(0,0,0,.18);overflow:hidden}
.p1{left:88px;top:120px}.p2{left:634px;top:126px}
.p3{left:88px;top:806px}.p4{left:634px;top:806px}
.p5{left:88px;top:1500px}.p6{left:634px;top:1500px}
.deco{position:absolute;inset:0;width:100%;height:100%;z-index:3;pointer-events:none}
.abs{position:absolute}
.copy{font-size:7.2px;line-height:1.3;text-align:justify}
.copy p{margin-bottom:7px}
.copy strong{font-weight:700}
.accent{color:var(--link)}
.logo-circle{left:333px;top:26px;width:124px;height:124px;border-radius:50%;background:#eef0f4;display:flex;align-items:center;justify-content:center;font-size:8px;color:var(--link)}
.badge{position:absolute;right:22px;top:20px;background:var(--red);color:#fff;font-family:"Oswald",Arial,sans-serif;font-weight:600;font-size:15px;letter-spacing:.2px;padding:3px 16px;border-radius:14px 4px 14px 4px;text-transform:uppercase;z-index:4}
.figure-box{border:1px solid #9fc3ea;padding:6px}
.figure-title{background:var(--cyan);color:#fff;font-weight:700;font-size:7.2px;text-align:center;padding:4px 6px;line-height:1.35;text-transform:uppercase}
.figure-title.big{font-size:9px}
.art{margin-top:6px;border-radius:2px}
.gmp-box{background:var(--cyan-light);color:#fff;padding:16px 18px;font-size:7.2px;line-height:1.32;text-align:justify;font-weight:700}
.table-title{font-size:6.4px;margin-bottom:7px}
.spec{width:100%;border-collapse:collapse;font-size:5.6px;color:#fff;font-weight:700}
.spec th{background:var(--navy);text-align:left;padding:2.5px 3px;border:1px solid #fff}
.spec td{padding:2.4px 3px;border:1px solid #fff;line-height:1.15}
.spec td:first-child{background:var(--row);width:31%}
.spec td:last-child{background:var(--green)}
</style>
</head>
<body>

<!-- Page 1: cover letter -->
<section class="page p1">
  <svg class="deco" viewBox="0 0 486 632" preserveAspectRatio="none" aria-hidden="true">
    <path d="M0 0H290C200 8 70 28 0 72Z" fill="var(--blue)"/>
    <path d="M0 54C60 26 150 12 220 8C140 20 60 40 0 72Z" fill="var(--cyan)"/>
    <path d="M0 560C150 590 330 565 486 505V632H0Z" fill="var(--cyan)"/>
    <path d="M0 585C170 615 350 585 486 535V632H0Z" fill="var(--red)"/>
    <path d="M0 598C180 625 360 598 486 552V632H0Z" fill="var(--blue)"/>
  </svg>
  <div class="abs logo-circle">LOGO</div>
  <div class="abs copy" style="left:29px;top:168px;width:430px">
    <p><strong>Dear Reader,</strong></p>
    <p><strong>Thank you for the opportunity to present our services and products.<br>Please review some information about our process and distribution, as well as some examples of products we can provide you with.</strong></p>
    <p>We work with NDAB Accredited Drug Distributors to ensure strict standards and compliance processes; this ensures that licensure verifications, operational policies, and procedures, as well as proper and approved Drugs, are distributed. The Accreditation was put in place to ensure end buyers, which are Pharmacies that the drugs purchased are not counterfeit and are coming from the Brands and Manufacturers directly.</p>
    <p>In short, the NDAB Accreditation is important because it ensures the drugs you are paying for are genuine articles. With the rise of counterfeit drugs and wholesale distributors, NDAB created these rules to combat illegitimate wholesalers. That's also why we offer pedigree tracing for our drugs so you can rest assured the drugs you order are the ones your receive.</p>
    <p>We have access to most, if not all, FDA Brand name and Generic Equivalent medications. To give you some examples, please see some of the top medications which are currently distributed in United States Pharmacies, we have included them at the end of this document as Attachment A.</p>
    <p><strong>Please provide us with a list of medications and quantities of the medication you are looking for; we will then reach out to our multiple warehouse distributors to find the best possible distributor to offer you as a possible option.</strong></p>
  </div>
  <div class="abs copy" style="left:29px;top:472px">COMPANY INFORMATION</div>
</section>

<!-- Page 2: buy and bill -->
<section class="page p2">
  <svg class="deco" viewBox="0 0 486 632" preserveAspectRatio="none" aria-hidden="true">
    <path d="M0 0H290C200 8 70 28 0 72Z" fill="var(--blue)"/>
    <path d="M0 54C60 26 150 12 220 8C140 20 60 40 0 72Z" fill="var(--cyan)"/>
    <path d="M0 560C150 590 330 565 486 505V632H0Z" fill="var(--cyan)"/>
    <path d="M0 585C170 615 350 585 486 535V632H0Z" fill="var(--red)"/>
    <path d="M0 598C180 625 360 598 486 552V632H0Z" fill="var(--blue)"/>
  </svg>
  <div class="badge">Buy &amp; Bill System</div>
  <div class="abs copy" style="right:26px;top:56px;width:380px;text-align:right">
    Our Clinic uses what is referred to in the industry as a <span class="accent"><strong>BUY AND BILL SYSTEM</strong></span>.<br>
    In this flowchart below, we are the CLINIC = us; we work with multiple Rx Wholesalers,<br>and in return, Rx Wholesalers work directly with Brands Manufacturers.
  </div>
  <div class="abs figure-box" style="left:26px;top:90px;width:432px;height:220px">
    <div class="figure-title">Distribution &amp; Reimbursementof Provider-Administered Outpatient Drugs:<br>Buy and Bill</div>
    <div class="art" role="img" aria-label="Flowchart of product movement, financial flow and contracts between manufacturer, wholesaler, provider clinic and health plan" style="height:168px;background:linear-gradient(135deg,#f4f7fb,#e3ebf5)"></div>
  </div>
  <div class="abs copy" style="left:29px;top:334px;width:428px">
    <p>Track and Trace is a method of following a product through the supply chain. In the pharmaceutical industry, this is often referred to as an e-pedigree. Government mandates to serialize pharmaceutical products are increasing around the globe. E-pedigree or electronic pedigree is an electronic version of the drug pedigree document. As defined by the U.S Food and Drug Administration as part of the 2006 Compliance Policy Guide for the Prescription Drug Marketing Act - " A drug pedigree is a statement of origin that identifies each prior sale, purchase, or trade of a drug, including the date of those transactions and the names and addresses of all parties to them."</p>
    <p><span class="accent">As a product moves from one place to the next, each company that handles the product must carry forward all of the previous e-pedigree information.</span> When it reaches it's final destination, the retailer will have a complete document showing where that shipment has been and who has handled that shipment. This is done for many reasons. The primary reason is for safety, it helps protect consumers from contaminated medicine and counterfeit drugs. It also has benefits to the manufacturer. Having the ability to serialize down to the unit level can help cut costs associated with recalls, as well as being able to more efficiently manage their shipments.</p>
    <p><span class="accent">The first critical piece of the chain occurs right on the packaging line.</span> Precise and consistent product handling, marking, inspection and data gathering are required to introduce accurate data into the front end of the system. Although pressure-sensitive labeling is the most common form of marking for bundles, cases and pallets, laser marking and ink jet coding are more common for units, because of space limitations and throughput speed requirements.</p>
  </div>
</section>

<!-- Page 3: manufacturing and GMP -->
<section class="page p3">
  <svg class="deco" viewBox="0 0 486 632" preserveAspectRatio="none" aria-hidden="true">
    <path d="M0 0H290C200 8 70 28 0 72Z" fill="var(--blue)"/>
    <path d="M0 54C60 26 150 12 220 8C140 20 60 40 0 72Z" fill="var(--cyan)"/>
    <path d="M0 560C150 590 330 565 486 505V632H0Z" fill="var(--cyan)"/>
    <path d="M0 585C170 615 350 585 486 535V632H0Z" fill="var(--red)"/>
    <path d="M0 598C180 625 360 598 486 552V632H0Z" fill="var(--blue)"/>
  </svg>
  <div class="abs copy" style="left:29px;top:68px;width:428px">
    <p>All manufacturing flows, whether making cars, pies, medical devices, or pharmaceuticals, take raw materials, and through a series of manufacturing processes, transform them into a final product. In pharmaceutical production the constituent parts include the active pharmaceutical ingredient (API), excipients, and packaging and labelling materials.</p>
    <p>Pharmaceuticals in tablet form may have coating agents added to make them easier to swallow and coloring to differentiate them. Tablets are often packaged in blister packs of 20 or so with a cardboard carton on which key consumer information is printed. As with cars or ice-cream each constituent part from the API to the foil of the blister pack must be traceable back to the originating batch of each originating supplier. If multiple batches of the same material are used this must become part of the production record. The key is traceability; traceability of everything that went into the batch of a product.</p>
  </div>
  <div class="abs gmp-box" style="left:29px;top:200px;width:216px;height:218px">
    The GMP principles put forward by the US Food and Drug Administration help ensure the quality of manufactured products throughout the manufacturing, processing and packaging stages. They are used to create a quality framework for the manufacture of a wide variety of products, including drugs, medical devices, some food, and blood, to make sure that the products are safe, pure and effective. GMP principles address a wide range of issues as varied as recordkeeping, personnel qualifications, sanitation, cleanliness, equipment verification, process validation, and complaint handling, but offer individual manufacturers the flexibility to decide how to implement the necessary controls in the most appropriate way for their particular business.
  </div>
  <div class="abs copy" style="left:264px;top:202px;width:192px">
    <p>Per US FDA, Good Manufacturing Practice (cGMP) and FDA 21 CFR Part 11 in pharmaceutical companies is a key regulatory requirements.</p>
    <p>To meet these GMP requirements is extremely important. The failure of organizations to comply with GMP regulations in any context can result in very serious consequences. These include internal direct costs related to product failure, scrap, etc and remediation costs related to problem identification, correction and reporting.</p>
    <p>There could also be significant external costs such as regulatory action costs related to recalls, discontinuation, suspended operations, etc. There may be costs associated with loss of market share due to reduced product volume. There is also the cost associated with damage to the company's reputation, which can even affect share value.</p>
  </div>
  <div class="abs" role="img" aria-label="Photograph of assorted pills and capsules scattered on white" style="left:20px;top:422px;width:300px;height:100px;background:radial-gradient(ellipse at 50% 55%,#e9c6c0 0%,#f1e3df 45%,#fff 75%)"></div>
</section>

<!-- Page 4: production line -->
<section class="page p4">
  <svg class="deco" viewBox="0 0 486 632" preserveAspectRatio="none" aria-hidden="true">
    <path d="M0 0H290C200 8 70 28 0 72Z" fill="var(--blue)"/>
    <path d="M0 54C60 26 150 12 220 8C140 20 60 40 0 72Z" fill="var(--cyan)"/>
    <path d="M0 560C150 590 330 565 486 505V632H0Z" fill="var(--cyan)"/>
    <path d="M0 585C170 615 350 585 486 535V632H0Z" fill="var(--red)"/>
    <path d="M0 598C180 625 360 598 486 552V632H0Z" fill="var(--blue)"/>
  </svg>
  <div class="abs figure-box" style="left:120px;top:30px;width:346px;height:216px">
    <div class="figure-title">Figure 1: Typical Pharmaceutical Tablet Production Line</div>
    <div class="art" role="img" aria-label="Technical drawing of a tablet production line: API and excipient hoppers, mill, granulator, dryer, tablet press, coater and packaging" style="height:182px;background:linear-gradient(135deg,#eef4fc,#dce8f7)"></div>
  </div>
  <div class="abs copy" style="left:29px;top:254px;width:428px">
    <p>An overview of a typical pharmaceutical tablet production line is shown in Figure 1. Like cooking, the exact proportions of the various raw ingredients are controlled by a recipe which defines the amount of API, and excipient required. The various ingredients may be milled and mixed to ensure an even distribution of API. Mixing can be performed as a slurry/wet mix which is dried and milled again to create a fine powder. This bulk powder may be mixed with further excipients before being formed into tablets in a tableting machine. The tablets may be coated and finally packaged as required.</p>
    <p>Testing will be performed at each critical stage of the flow from raw materials to the final packaged product. For example, the incoming raw materials may be re-tested to ensure they conform to the supplier's specification before being released for use. The output of the granulator may be tested to ensure the API is evenly mixed and the output from the milling checked to ensure the mixture still contains the correct proportions of API and is ground evenly. Samples of tablet from the final product are retained for dissolution, stability, and other quality assurance purposes.</p>
    <p>All LIMS require the ability to track samples and associated test results, create certificates of analysis (CofA), use barcoding and associate samples with key information such as batch and supplier. LIMS will also include the ability to manage calibration and maintenance of laboratory instruments, and records which instruments were used for each sample test, along with who tested that sample and whether they were competent to test it, and to control inventory of the chemicals and the laboratory consumables used in testing.</p>
    <p>But while a typical QC sampling flow monitors and reports on discreet samples, a manufacturing flow requires a broader range of information to be associated and combined for management and reporting. A manufacturing flow requires the addition of Recipe Management to control the raw materials and intermediate products going into each manufacturing batch; the ability to keep test results for each part of the flow (raw materials, intermediate stages and final product); to link test results to the originating raw materials/suppliers and final product/customers; the statistical tools to control the process within defined limits; and the ability to quickly retrieve and report on this data.</p>
  </div>
</section>

<!-- Page 5: LIMS workflow -->
<section class="page p5">
  <svg class="deco" viewBox="0 0 486 632" preserveAspectRatio="none" aria-hidden="true">
    <path d="M0 0H290C200 8 70 28 0 72Z" fill="var(--blue)"/>
    <path d="M0 54C60 26 150 12 220 8C140 20 60 40 0 72Z" fill="var(--cyan)"/>
    <path d="M0 560C150 590 330 565 486 505V632H0Z" fill="var(--cyan)"/>
    <path d="M0 585C170 615 350 585 486 535V632H0Z" fill="var(--red)"/>
    <path d="M0 598C180 625 360 598 486 552V632H0Z" fill="var(--blue)"/>
  </svg>
  <div class="abs copy" style="left:202px;top:20px;width:262px">
    Laboratory information management systems (LIMS) are used extensively in laboratories in a huge number of industries to manage, track and report on samples, tests, test results and more. In manufacturing industries laboratory testing can be involved at every step, from raw material analysis through to the finished product
  </div>
  <div class="abs figure-box" style="left:24px;top:78px;width:440px;height:326px">
    <div class="figure-title big">Nuvora Health LIMS Workflow</div>
    <div class="art" role="img" aria-label="Circular workflow diagram: sample reception, batching, preparation, results capture, quality control, verification, publication, query and analysis request" style="height:286px;background:radial-gradient(circle at 50% 50%,#f3f6fb,#e6edf6)"></div>
  </div>
  <div class="abs" role="img" aria-label="Photograph of a laboratory scientist working with blue test liquid" style="left:30px;top:420px;width:330px;height:150px;background:linear-gradient(90deg,#ffffff,#dfeaf6 40%,#c9dcef 60%,#ffffff)"></div>
</section>

<!-- Page 6: LIMS key elements -->
<section class="page p6">
  <svg class="deco" viewBox="0 0 486 632" preserveAspectRatio="none" aria-hidden="true">
    <path d="M0 0H290C200 8 70 28 0 72Z" fill="var(--blue)"/>
    <path d="M0 54C60 26 150 12 220 8C140 20 60 40 0 72Z" fill="var(--cyan)"/>
    <path d="M0 560C150 590 330 565 486 505V632H0Z" fill="var(--cyan)"/>
    <path d="M0 585C170 615 350 585 486 535V632H0Z" fill="var(--red)"/>
    <path d="M0 598C180 625 360 598 486 552V632H0Z" fill="var(--blue)"/>
  </svg>
  <div class="badge" style="top:36px">Key Elements of a Manufacturing LIMS</div>
  <div class="abs" style="left:36px;top:86px;width:418px">
    <div class="table-title">Key elements specific to the pharmaceutical manufacturing LIMS include:</div>
    <table class="spec">
      <tr><th>Element</th><th>Description</th></tr>
      <tr><td>Materials Management</td><td>Defines raw, intermediate and final products (RM, IP and FP) used or manufactured</td></tr>
      <tr><td>Supplier Management</td><td>Manages suppliers and defines the raw materials they supply</td></tr>
      <tr><td>Recipe Management</td><td>Identifies the component materials that go into the products (IP or FP)</td></tr>
      <tr><td>Batch Management</td><td>Defines the ways that batch manufacture is handled in the LIMS</td></tr>
      <tr><td>Batch Genealogy</td><td>Controls the ability to track and trace component materials for a product</td></tr>
      <tr><td>Test Management</td><td>Defines the testing that the batches will undergo</td></tr>
      <tr><td>Specification Management</td><td>Describes the manufacturing specifications the batches must be tested against</td></tr>
    </table>
  </div>
  <div class="abs" style="left:36px;top:252px;width:418px">
    <div class="table-title">Other key elements include:</div>
    <table class="spec">
      <tr><th>Element</th><th>Description</th></tr>
      <tr><td>ICMS Management</td><td>Instrument calibration and maintenance management and tracking</td></tr>
      <tr><td>Competency Management</td><td>Tracking and management of analyst training and certifications</td></tr>
      <tr><td>CAPA Management</td><td>Corrective and Preventive actions for the quality cycle</td></tr>
      <tr><td>Product Grading</td><td>Allows the grading of a product against alternative and possibly multiple specifications</td></tr>
      <tr><td>Frequency Testing</td><td>Implement reduced testing regimes based on previous results or experience, especially useful for raw materials and trusted suppliers</td></tr>
      <tr><td>Environmental Monitoring</td><td>Monitor the production environment to ensure cleanliness</td></tr>
      <tr><td>Stability Management</td><td>Manages the storage and shelf-life/QA testing of product samples</td></tr>
    </table>
  </div>
  <div class="abs" role="img" aria-label="Illustration of interlocking gears filled with medical and healthcare icons" style="left:108px;top:408px;width:290px;height:120px;background:radial-gradient(ellipse at 50% 50%,#5fb6e6 0%,#2f7fc6 45%,#ffffff 78%)"></div>
</section>

</body>
</html>
```